6 Page Brochure for Car Dealers

1. We are an an accident management company in Sydney. Our website is wheelfix.com.au. We provide services for car dealers.

2. We need a 6 page brochure which we can leave with car dealers after we visit them. An example of what we are after is at :
http://www.layoutnest.com/wp-content/uploads/2014/02/Zo-Trend-Auto-Shine-brochure-1.jpg
http://www.layoutnest.com/wp-content/uploads/2014/02/Zo-Trend-Auto-Shine-brochure-3.jpg

3. The layout of the brochure is proposed as follows:

Page 1 - Title page with our logo, visual representation of a happy car dealer, and call to action such as "Try accident management to supercharge profits"

Page 2 - Qualifier page - compares a successful dealership vs an unsuccessful dealership...need a comparison layout similar to this:

https://img-store-bx3.snapboardia.com/736x/a1/42/93/a1429375bd2e6c1047fa3b815ec2d7a9.jpg

Page 3 - Benefits page which shows the customer's journey
Something similar to:

https://www.ridgeservers.com/wp-content/uploads/2015/03/rs-benefits-pdf.png/

Page 4: How to get started page which identifies a four step process: signing agreement, us providing training, reporting accidents using an online portal, collecting payment from us.

Page 5: Testimonials page from other dealerships
Visual logos of our different smash repairer partners

Page 6: Team and contact page with group shot of our whole company, map of where our office is located and office contact details.

Please let us know if you may design something for us.

Target Market(s)

Car dealers

Industry/Entity Type

Car Dealer

Font styles to use
Sans Serif

Colors
f04a50
ec1f27
f59296
fbd4d5

Requirements
Must have
• Please project description
Nice to have

```html
<!DOCTYPE html>
<html lang="en">
<head>
<meta charset="utf-8">
<title>WHEELFIX – How to Get Started Brochure Spread</title>
<link rel="stylesheet" href="https://fonts.googleapis.com/css2?family=Open+Sans:wght@400;600;700&family=Oswald:wght@400;600;700&display=swap">
<style>
  :root {
    --red: #ec1f27;
    --red-soft: #f04a50;
    --pink: #f59296;
    --pink-pale: #fbd4d5;
    --ink: #2b2b2d;
    --ink-deep: #231f20;
    --paper: #ffffff;
    --backdrop: #e4e4e7;
  }
  * { box-sizing: border-box; margin: 0; padding: 0; }
  html, body {
    width: 1200px; height: 702px; overflow: hidden;
    background: var(--backdrop);
    font-family: "Open Sans", Arial, sans-serif;
    color: var(--ink);
  }
  .brochure {
    position: absolute; left: 40px; top: 71px;
    width: 1120px; height: 560px;
    background: var(--paper);
    box-shadow: 0 6px 18px rgba(0,0,0,.18);
    overflow: hidden;
  }
  .panel { position: absolute; top: 0; width: 560px; height: 560px; overflow: hidden; }
  .panel--steps { left: 0; }
  .panel--cover { left: 560px; }

  /* ---------- steps panel ---------- */
  .steps-ribbon { position: absolute; inset: 0; }
  .step { position: absolute; height: 60px; }
  .step__bar {
    position: absolute; left: 0; top: 12px; height: 38px;
    background: var(--ink);
    border-right: 8px solid var(--pink-pale);
    border-radius: 3px;
    color: #fff; font-size: 14px; font-weight: 600;
    padding-left: 78px; display: flex; align-items: center; line-height: 1.15;
  }
  .step__badge {
    position: absolute; left: 14px; top: 0; width: 56px; height: 60px;
    background: var(--pink-pale);
    border: 2px solid var(--pink);
    text-align: center; color: var(--red);
    font-family: "Oswald", sans-serif; line-height: 1;
  }
  .step__label { display: block; font-size: 13px; padding-top: 5px; }
  .step__num { display: block; font-size: 30px; font-weight: 600; }
  .step--1 { left: 96px;  top: 36px;  width: 340px; }
  .step--2 { left: 140px; top: 96px;  width: 340px; }
  .step--3 { left: 186px; top: 158px; width: 350px; }
  .step--4 { left: 232px; top: 222px; width: 350px; }
  .step--4 .step__bar { border-right: none; }

  .intro-title { position: absolute; left: 28px; top: 176px; line-height: 1.1; }
  .intro-title__lead { display: block; color: var(--red); font-size: 19px; font-weight: 600; }
  .intro-title__main { display: block; color: var(--ink); font-size: 25px; font-weight: 600; }

  .contact { position: absolute; left: 28px; top: 318px; font-size: 11px; line-height: 1.45; }
  .contact__heading {
    font-family: "Oswald", sans-serif; color: var(--red-soft);
    font-size: 19px; font-weight: 400; margin-bottom: 6px;
  }
  .contact__line--gap { margin-top: 6px; }
  .divider { position: absolute; left: 406px; top: 306px; width: 1px; height: 102px; background: #9a9a9a; }
  .wordmark {
    font-family: "Oswald", sans-serif; font-weight: 600;
    color: var(--ink-deep); letter-spacing: .5px;
  }
  .panel--steps .wordmark { position: absolute; left: 432px; top: 342px; font-size: 26px; }
  .base-band { position: absolute; left: 0; bottom: 0; width: 560px; height: 30px; background: var(--ink); }

  /* ---------- cover panel ---------- */
  .cover-art { position: absolute; inset: 0; }
  .panel--cover .wordmark { position: absolute; right: 28px; top: 12px; font-size: 28px; }
  .call-badge {
    position: absolute; left: 50px; top: 210px; width: 140px; height: 140px;
    border-radius: 50%; background: #fff;
    border: 6px solid var(--red);
    box-shadow: 0 0 0 4px #fff, 0 0 0 6px #c8c8c8;
    display: flex; flex-direction: column; align-items: center; justify-content: center;
    font-family: "Oswald", sans-serif; text-align: center; line-height: 1.15;
  }
  .call-badge__label { color: var(--red); font-size: 18px; font-weight: 600; }
  .call-badge__number { color: var(--ink); font-size: 20px; }
  .headline { position: absolute; left: 36px; top: 412px; color: #fff; }
  .headline__lead { display: block; font-size: 23px; font-weight: 400; }
  .headline__main {
    display: block; font-family: "Oswald", sans-serif; font-weight: 700;
    font-size: 50px; line-height: 1.05;
  }
  .headline__url { display: block; font-size: 11px; letter-spacing: 7px; margin-top: 6px; }
</style>
</head>
<body>
<main class="brochure">

  <section class="panel panel--steps">
    <svg class="steps-ribbon" viewBox="0 0 560 560" aria-hidden="true">
      <polygon points="150,44 190,44 540,372 500,372" fill="#ec1f27"/>
      <polygon points="478,350 560,350 530,418" fill="#ec1f27"/>
    </svg>

    <div class="step step--1">
      <div class="step__bar">Signing agreement</div>
      <div class="step__badge"><span class="step__label">STEP</span><span class="step__num">01</span></div>
    </div>
    <div class="step step--2">
      <div class="step__bar">Providing training</div>
      <div class="step__badge"><span class="step__label">STEP</span><span class="step__num">02</span></div>
    </div>
    <div class="step step--3">
      <div class="step__bar">Reporting accidents using<br>an online portal</div>
      <div class="step__badge"><span class="step__label">STEP</span><span class="step__num">03</span></div>
    </div>
    <div class="step step--4">
      <div class="step__bar">Collecting payment from us</div>
      <div class="step__badge"><span class="step__label">STEP</span><span class="step__num">04</span></div>
    </div>

    <h2 class="intro-title">
      <span class="intro-title__lead">HOW TO GET</span>
      <span class="intro-title__main">STARTED?</span>
    </h2>

    <address class="contact" style="font-style:normal">
      <h3 class="contact__heading">CONTACT US:</h3>
      <p>Suite 12, Lv 3, 88 Harrow St SYDNEY</p>
      <p>PO Box 40517 Harbour Point NSW 2000</p>
      <p class="contact__line--gap">contact@wheelfix.com.au</p>
      <p>www.wheelfix.com</p>
    </address>
    <div class="divider"></div>
    <div class="wordmark">WHEELFIX</div>
    <div class="base-band"></div>
  </section>

  <section class="panel panel--cover">
    <svg class="cover-art" viewBox="0 0 560 560">
      <defs>
        <linearGradient id="sceneTone" x1="0" y1="0" x2="1" y2="1">
          <stop offset="0" stop-color="#c9ccd3"/>
          <stop offset=".5" stop-color="#9aa0ad"/>
          <stop offset="1" stop-color="#5d6270"/>
        </linearGradient>
      </defs>
      <polygon points="0,40 300,40 560,104 560,560 0,560" fill="url(#sceneTone)"
               role="img" aria-label="Photo: smiling car dealer in a suit handing a new car to a happy woman at the wheel"/>
      <polygon points="300,40 560,104 560,116 290,48" fill="#2b2b2d"/>
      <polygon points="0,300 470,368 560,368 560,560 0,560" fill="#ec1f27"/>
      <polygon points="0,300 470,368 0,340" fill="#c9161d"/>
      <polygon points="400,560 560,402 560,560" fill="#2b2b2d"/>
    </svg>

    <div class="wordmark">WHEELFIX</div>

    <div class="call-badge">
      <span class="call-badge__label">CALL US NOW:</span>
      <span class="call-badge__number">1300 FIXIT 5</span>
    </div>

    <h1 class="headline">
      <span class="headline__lead">Try accident management</span>
      <span class="headline__main">to supercharge profits</span>
      <span class="headline__url">www.wheelfix.com.au</span>
    </h1>
  </section>

</main>
</body>
</html>
```